Design a large parking banner – mandatory ticket validation in the shop

Banner Size:
548 cm (width) x 154 cm (height)
Note: The banner will be placed in a metal frame at our parking lot entrance, fully visible to every incoming truck driver. The message must be easy to read from a distance.
Goal of the Banner:
To inform all truck drivers that they must validate their entry ticket inside the shop, even if they are parking for a short time.
The message must be displayed in multiple languages for international drivers.
Mandatory Content:
Main message – in multiple languages (clearly separated or stacked):
Dutch (NL): Vergeet je ticket niet te valideren in de shop – verplicht, ook bij kort parkeren!
French (FR): N'oubliez pas de valider votre ticket à la boutique – obligatoire, même pour un court arrêt !
English (EN): Don't forget to validate your entry ticket in the shop – mandatory, even for short stops!
German (DE): Vergessen Sie nicht, Ihr Einfahrticket im Shop zu entwerten – Pflicht, auch bei kurzem Parken!
Polish (PL): Nie zapomnij zatwierdzić biletu w sklepie – obowiązkowe, nawet przy krótkim postoju!
Romanian (RO): Nu uitați să validați biletul în magazin – obligatoriu, chiar și pentru opriri scurte!
You can include more languages if space allows, but these are essential.
Opening Hours Block (in one section below):
Shop Opening Hours
Mon – Fri: 05:30 – 22:00
Sat & Sun: 08:00 – 22:00
Style & Branding:
The design must match the visual identity of Haulpoint 41Ter
Please refer to the attached photos of existing parking signage for guidance on colors, typography, and layout style
Our logo (attached) must be clearly visible and professionally integrated
Feel free to use icons or pictograms to visually support the message (e.g., ticket, truck, arrow)
Readability is key – large, bold text and high contrast colors that are visible from a distance
Target Audience:
International truck drivers – people who need fast, clear communication. Not everyone speaks the local language, so visual clarity and multilingual messaging are critical.
File Requirements:
Print-ready file (PDF or EPS) – 300 dpi at 1:10 scale
Include 5 cm bleed on all sides
Provide open source files if possible (AI or PSD)

```html
<!DOCTYPE html>
<html lang="en">
<head>
<meta charset="utf-8">
<title>Haulpoint 41Ter – Parking Ticket Banner</title>
<link href="https://fonts.googleapis.com/css2?family=Poppins:wght@600;700;800&display=swap" rel="stylesheet">
<style>
  :root {
    --page: #e6e6e6;
    --navy: #37385f;
    --blue: #2f80c6;
    --red: #ff0000;
    --label-red: #e8121b;
    --white: #ffffff;
  }
  html, body {
    margin: 0;
    width: 1200px;
    height: 380px;
    overflow: hidden;
    background: var(--page);
    font-family: 'Poppins', sans-serif;
  }
  .banner {
    position: absolute;
    left: 35px;
    top: 28px;
    width: 1128px;
    height: 317px;
    background: var(--navy);
    color: var(--white);
  }
  .brand-name {
    position: absolute;
    left: 100px;
    top: 38px;
    margin: 0;
    font-weight: 800;
    font-size: 58px;
    line-height: 0.95;
    letter-spacing: -1.5px;
    text-transform: uppercase;
    color: var(--white);
  }
  .brand-name .brand-line { display: block; }
  .brand-name .brand-sub { font-size: 52px; padding-left: 150px; }

  .parking-sign {
    position: absolute;
    left: 35px;
    top: 197px;
    width: 28px;
    height: 40px;
    background: var(--blue);
    border-radius: 4px;
    border: 1px solid #1f5f99;
    font-weight: 800;
    font-size: 34px;
    line-height: 40px;
    text-align: center;
  }
  .parking-label {
    position: absolute;
    left: 77px;
    top: 200px;
    font-weight: 700;
    font-size: 27px;
    line-height: 36px;
    letter-spacing: 0.5px;
  }
  .chevron {
    position: absolute;
    left: 90px;
    top: 259px;
  }
  .ticket-label {
    position: absolute;
    left: 192px;
    top: 234px;
    font-weight: 700;
    font-size: 37px;
    line-height: 46px;
    letter-spacing: 0.5px;
  }
  .ticket-area {
    position: absolute;
    left: 372px;
    top: 236px;
    width: 96px;
    height: 48px;
    background: var(--white);
    border-radius: 4px;
  }

  .messages {
    position: absolute;
    left: 500px;
    top: 16px;
    margin: 0;
    padding: 0;
    list-style: none;
  }
  .messages li {
    font-weight: 700;
    font-size: 11.7px;
    letter-spacing: -0.45px;
    line-height: 25.4px;
    white-space: nowrap;
  }
  .messages .lang { color: var(--label-red); font-weight: 600; }

  .hours {
    position: absolute;
    left: 507px;
    top: 185px;
    width: 594px;
  }
  .hours-bar {
    height: 36px;
    background: var(--blue);
    border: 1px solid #1f5f99;
    box-sizing: border-box;
    font-weight: 700;
    font-size: 24px;
    line-height: 34px;
    text-align: center;
  }
  .hours-row {
    display: flex;
    margin: 4px 0 9px;
    height: 32px;
  }
  .hours-cell {
    background: var(--red);
    font-weight: 700;
    font-size: 24px;
    line-height: 32px;
    white-space: nowrap;
  }
  .hours-cell.weekdays { width: 296px; padding-left: 7px; box-sizing: border-box; }
  .hours-cell.weekend { flex: 1; margin-left: 1px; padding-left: 6px; }
</style>
</head>
<body>
  <main class="banner">
    <h1 class="brand-name"><span class="brand-line">Haulpoint</span><span class="brand-line brand-sub">41Ter</span></h1>

    <div class="parking-sign" aria-hidden="true">P</div>
    <div class="parking-label">TRUCKS</div>
    <svg class="chevron" width="52" height="32" viewBox="0 0 52 32" aria-hidden="true">
      <polygon points="0,0 26,18 52,0 52,14 26,32 0,14" fill="var(--white)"/>
    </svg>
    <div class="ticket-label">+ TICKET</div>
    <div class="ticket-area" role="img" aria-label="Parking ticket pictogram"></div>

    <ul class="messages">
      <li><span class="lang">Dutch (NL):</span> Vergeet je ticket niet te valideren in de shop – verplicht, ook bij kort parkeren!</li>
      <li><span class="lang">French (FR):</span> N'oubliez pas de valider votre ticket à la boutique – obligatoire, même pour un court arrêt !</li>
      <li><span class="lang">English (EN):</span> Don't forget to validate your entry ticket in the shop – mandatory, even for short stops!</li>
      <li><span class="lang">German (DE):</span> Vergessen Sie nicht, Ihr Einfahrticket im Shop zu entwerten – Pflicht, auch bei kurzem Parken!</li>
      <li><span class="lang">Polish (PL):</span> Nie zapomnij zatwierdzić biletu w sklepie – obowiązkowe, nawet przy krótkim postoju!</li>
      <li><span class="lang">Romanian (RO):</span> Nu uitați să validați biletul în magazin – obligatoriu, chiar și pentru opriri scurte!</li>
    </ul>

    <section class="hours">
      <div class="hours-bar">Shop Opening Hours</div>
      <div class="hours-row">
        <div class="hours-cell weekdays">Mon – Fri: 05:30 – 22:00</div>
        <div class="hours-cell weekend">Sat &amp; Sun: 08:00 – 22:00</div>
      </div>
      <div class="hours-bar">Style &amp; Branding:</div>
    </section>
  </main>
</body>
</html>
```